Rise As Captain Book Cover Design

Book Cover Design Brief
Book Title
Rise As Captain
Subtitle
The 12 Quiet Pillars of Remarkable Command
Author
Orwen Talbrisk
Overview
This book is about leadership that starts within.
Most leadership books focus on tactics or management strategies. This book focuses on the inner disciplines that create powerful leaders — mindset, integrity, focus, empathy, professionalism, honesty, and self-respect.
The tone of the book is bold, direct, confident, and transformational.
This is not a soft or corporate leadership book. It is a call to step up and become the leader you are capable of becoming.
The cover should feel:
• Powerful
• Professional
• Transformational
• Premium
• Memorable
Think best-selling leadership book, not a generic business book.
Target Audience
Business owners
Managers
Entrepreneurs
Team leaders
Professionals who want to grow as leaders
Most readers are ambitious professionals who want to level up their leadership and life.
Design Direction
The design should communicate:
Strength. Discipline. Leadership. Personal transformation.
Avoid cliché leadership visuals like:
• Handshakes
• Office buildings
• Corporate stock imagery
• Teams sitting around tables
The design should feel iconic, bold, and timeless.
Think about covers of successful leadership books such as:
Tiny Rituals
Total Custody
Won't Bend Now
Begin From Core
The 52 Codes of Sway
These covers are simple, powerful, and recognizable even at small sizes.
Typography
The title RISE AS CAPTAIN should be:
• Bold
• Strong
• Dominant on the cover
• Easy to read even at small sizes (important for Quillora thumbnails)
The subtitle should be clean and secondary to the title.
The overall typography should feel strong, modern, and premium.
Color Direction
Designers are free to explore colors, but the cover should feel strong and premium, not playful.
Colors that often work well for leadership books include:
Black
Gold
White
Deep blue
Dark red
High contrast and clarity are important.
Style
Preferred style:
• Clean
• Modern
• Minimal
• Strong contrast
Avoid clutter and overly busy designs.
The goal is to create a cover that feels powerful and professional at first glance.
Deliverables
Front cover design for a leadership book.
Final files should include:
• High resolution artwork
• Editable source files
• Print-ready version suitable for publishing
Goal of the Cover
When someone sees this book on Quillora or in a bookstore, they should immediately think:
“This looks like a serious leadership book.”
The design should feel like it belongs next to books by authors such as:
Marcus Dovell
Brant Feltham
Owen Marsh
Peter Halvorn
A strong, confident cover that attracts leaders who want to grow and perform at a higher level.
Updates
Target Market(s)
Business Owners and High level managers
Look and feel

```html
<!DOCTYPE html>
<html lang="en">
<head>
<meta charset="UTF-8">
<title>Rise As Captain — Book Cover</title>
<link rel="stylesheet" href="https://fonts.googleapis.com/css2?family=Bebas+Neue&family=Cinzel:wght@400;700;900&display=swap">
<style>
  :root {
    --navy-top: #1e2362;
    --navy-mid: #161a50;
    --navy-bottom: #080b2b;
    --gold-light: #e5c560;
    --gold-mid: #b0923d;
    --gold-dark: #654a08;
    --gold-deep: #8b6508;
    --ink-white: #ffffff;
  }
  html, body {
    margin: 0;
    padding: 0;
    width: 846px;
    height: 1200px;
    overflow: hidden;
    background: var(--navy-bottom);
  }
  .cover {
    position: relative;
    width: 846px;
    height: 1200px;
    overflow: hidden;
    background: linear-gradient(178deg, var(--navy-top) 0%, var(--navy-top) 25%, var(--navy-mid) 55%, var(--navy-bottom) 100%);
  }
  .title-art {
    position: absolute;
    left: 0;
    top: 0;
    width: 846px;
    height: 760px;
  }
  .title-line {
    font-family: "Bebas Neue", "Anton", sans-serif;
  }
  .subtitle {
    position: absolute;
    left: 0;
    right: 0;
    top: 752px;
    margin: 0;
    text-align: center;
    font-family: "Cinzel", serif;
    font-weight: 400;
    font-size: 35px;
    line-height: 58px;
    letter-spacing: 1px;
    color: var(--ink-white);
  }
  .subtitle .numeral {
    font-weight: 900;
  }
  .author {
    position: absolute;
    left: 0;
    right: 0;
    top: 1000px;
    margin: 0;
    text-align: center;
    font-family: "Cinzel", serif;
    font-weight: 900;
    font-size: 66px;
    letter-spacing: 0;
    color: var(--ink-white);
  }
</style>
</head>
<body>
  <main class="cover">
    <svg class="title-art" viewBox="0 0 846 760" xmlns="http://www.w3.org/2000/svg">
      <defs>
        <linearGradient id="goldTop" gradientUnits="userSpaceOnUse" x1="0" y1="70" x2="30" y2="380">
          <stop offset="0" stop-color="var(--gold-light)"/>
          <stop offset="0.3" stop-color="var(--gold-mid)"/>
          <stop offset="0.6" stop-color="var(--gold-dark)"/>
          <stop offset="1" stop-color="var(--gold-deep)"/>
        </linearGradient>
        <linearGradient id="goldBottom" gradientUnits="userSpaceOnUse" x1="0" y1="440" x2="30" y2="705">
          <stop offset="0" stop-color="var(--gold-light)"/>
          <stop offset="0.3" stop-color="var(--gold-mid)"/>
          <stop offset="0.6" stop-color="var(--gold-dark)"/>
          <stop offset="1" stop-color="var(--gold-deep)"/>
        </linearGradient>
      </defs>
      <text class="title-line" x="-8" y="375" font-size="445" textLength="872" lengthAdjust="spacingAndGlyphs" fill="url(#goldTop)">RISE AS</text>
      <text class="title-line" x="-8" y="703" font-size="368" textLength="872" lengthAdjust="spacingAndGlyphs" fill="url(#goldBottom)">CAPTAIN</text>
    </svg>

    <p class="subtitle">THE <span class="numeral">12</span> QUIET PILLARS<br>OF REMARKABLE COMMAND</p>

    <p class="author">Orwen Talbrisk</p>
  </main>
</body>
</html>
```